Business Cards for a small business advisory (business services)

Professional look. Same as would apply for a lawyer, accountant, or other financial services professional. Please use the logo colors

Target Market(s)

small business owners

Industry/Entity Type

Financial Servics

Contact Information for Business Card

Name: Gavin L. Whitmore, CAIA / Title: Business Advisor / Office #: (718) 294-7716 / Mobile #: (917) 382-5047 / Email: g.whitmore@clearfieldventurepartners.example / Web: www.clearfieldventurepartners.example

Font styles to use
Sans Serif

```html
<!DOCTYPE html>
<html lang="en">
<head>
<meta charset="utf-8">
<title>Clearfield Venture Partners – Business Card</title>
<link rel="stylesheet" href="https://fonts.googleapis.com/css2?family=Figtree:wght@400;500;600;700&display=swap">
<style>
  :root {
    --navy: #1d3a69;
    --green: #8cc63f;
    --paper: #ffffff;
    --backdrop: #f3f4f6;
  }
  * { box-sizing: border-box; margin: 0; padding: 0; }
  html, body {
    width: 1200px; height: 1200px; overflow: hidden;
    background: var(--backdrop);
    font-family: "Figtree", sans-serif;
  }
  .sheet {
    width: 1200px; height: 1200px;
    display: flex; flex-direction: column; align-items: center; justify-content: center;
    gap: 30px;
  }
  .card {
    position: relative;
    width: 860px; height: 557px;
  }
  .card--front {
    background: var(--navy);
    display: flex; align-items: center; justify-content: center;
  }
  .wordmark {
    display: flex; align-items: center; gap: 18px;
    font-weight: 700; letter-spacing: 0.2px;
  }
  .wordmark__dot { border-radius: 50%; flex: none; }
  .card--front .wordmark { font-size: 44px; color: var(--paper); }
  .card--front .wordmark__dot { width: 48px; height: 48px; background: var(--paper); }

  .card--back {
    background: var(--paper);
    border: 1px solid #e4e6ea;
  }
  .card--back .wordmark {
    position: absolute; top: 66px; right: 70px;
    font-size: 22px; color: var(--navy); gap: 10px;
  }
  .card--back .wordmark__dot { width: 26px; height: 26px; background: var(--navy); }

  .identity {
    position: absolute; right: 472px; top: 244px;
    text-align: right; color: var(--navy);
  }
  .identity__name { font-size: 34px; font-weight: 600; white-space: nowrap; }
  .identity__cred { color: var(--green); font-weight: 500; }
  .identity__title { font-size: 20px; font-weight: 400; margin-top: 4px; }

  .divider {
    position: absolute; left: 405px; top: 224px;
    width: 2px; height: 148px;
    background: linear-gradient(to bottom, rgba(140,198,63,0), var(--green) 15%, var(--green) 85%, rgba(140,198,63,0));
  }
  .contact {
    position: absolute; left: 428px; top: 220px;
    list-style: none; color: var(--navy);
  }
  .contact__item {
    display: flex; align-items: center; gap: 12px;
    height: 30px; margin-bottom: 11px;
    font-size: 17px; white-space: nowrap;
  }
  .contact__icon { width: 20px; height: 20px; flex: none; fill: var(--navy); }
</style>
</head>
<body>
<main class="sheet">
  <section class="card card--front" aria-label="Card front">
    <div class="wordmark"><span class="wordmark__dot"></span><span>Clearfield Venture Partners</span></div>
  </section>

  <section class="card card--back" aria-label="Card back">
    <div class="wordmark"><span class="wordmark__dot"></span><span>Clearfield Venture Partners</span></div>

    <div class="identity">
      <p class="identity__name">Gavin L. Whitmore, <span class="identity__cred">CAIA</span></p>
      <p class="identity__title">Business Advisor</p>
    </div>

    <div class="divider"></div>

    <ul class="contact">
      <li class="contact__item">
        <svg class="contact__icon" viewBox="0 0 24 24" aria-hidden="true"><path d="M6.6 10.8a15.1 15.1 0 0 0 6.6 6.6l2.2-2.2a1 1 0 0 1 1-.25 11.4 11.4 0 0 0 3.6.57 1 1 0 0 1 1 1V20a1 1 0 0 1-1 1A17 17 0 0 1 3 4a1 1 0 0 1 1-1h3.5a1 1 0 0 1 1 1c0 1.25.2 2.45.57 3.57a1 1 0 0 1-.25 1z"/></svg>
        <span>(718) 294-7716</span>
      </li>
      <li class="contact__item">
        <svg class="contact__icon" viewBox="0 0 24 24" aria-hidden="true"><path d="M8 1.5h8A2.5 2.5 0 0 1 18.5 4v16a2.5 2.5 0 0 1-2.5 2.5H8A2.5 2.5 0 0 1 5.5 20V4A2.5 2.5 0 0 1 8 1.5zm0 2a.5.5 0 0 0-.5.5v13.5h9V4a.5.5 0 0 0-.5-.5zM12 18.6a1.1 1.1 0 1 0 0 2.2 1.1 1.1 0 0 0 0-2.2z"/></svg>
        <span>(917) 382-5047</span>
      </li>
      <li class="contact__item">
        <svg class="contact__icon" viewBox="0 0 24 24" aria-hidden="true"><path d="M3 5h18a1 1 0 0 1 1 1v12a1 1 0 0 1-1 1H3a1 1 0 0 1-1-1V6a1 1 0 0 1 1-1zm1 2.4V17h16V7.4l-8 5.3zM5.6 7 12 11.2 18.4 7z"/></svg>
        <span>g.whitmore@clearfieldventurepartners.example</span>
      </li>
      <li class="contact__item">
        <svg class="contact__icon" viewBox="0 0 24 24" aria-hidden="true"><path d="M12 2a10 10 0 1 0 0 20 10 10 0 0 0 0-20zm6.9 6h-3a15.6 15.6 0 0 0-1.4-3.6A8 8 0 0 1 18.9 8zM12 4c.8 1.2 1.5 2.5 1.9 4h-3.8c.4-1.5 1.1-2.8 1.9-4zM4.3 14a8.2 8.2 0 0 1 0-4h3.4a16.5 16.5 0 0 0 0 4zm.8 2h3a15.6 15.6 0 0 0 1.4 3.6A8 8 0 0 1 5.1 16zm3-8h-3a8 8 0 0 1 4.4-3.6A15.6 15.6 0 0 0 8.1 8zM12 20c-.8-1.2-1.5-2.5-1.9-4h3.8c-.4 1.5-1.1 2.8-1.9 4zm2.3-6H9.7a14.7 14.7 0 0 1 0-4h4.6a14.7 14.7 0 0 1 0 4zm.2 5.6a15.6 15.6 0 0 0 1.4-3.6h3a8 8 0 0 1-4.4 3.6zm1.8-5.6a16.5 16.5 0 0 0 0-4h3.4a8.2 8.2 0 0 1 0 4z"/></svg>
        <span>www.clearfieldventurepartners.example</span>
      </li>
    </ul>
  </section>
</main>
</body>
</html>
```